Lumacraftery 'Quiet Harbour' Book Cover Design project

I need to revise the book cover design I have for my coming book. The design I created through PixelGuild is great but the book has grown and changed so I'm looking for an alternative/option design. I can then choose later from the different options.

I need a book cover that represents the unique book I am creating.

Book Title:
The Open Meadow

Subtitle: Walking Forward Beyond Every Box

The book is targeting all readers with a special focus on same sex attracted readers. It should not have stereotypical images.

I am including a file of the book cover I have had designed. The back cover blurb, author info and author pic will remain the same. The colouring of the back cover and spine will, of course, change to match the colouring of the front cover.

The new title will be on the spine and the new title wording.

The front cover will be markedly different using the bold images and rainbow colours of the images found in the files I am uploading for you.

I am thinking of a large boldly coloured rainbow face with the title and subtitle ON the image. The image will be the whole cover. It will fill the cover as much as possible with the text added onto the pic.

The bold pictures I am including will give you the idea of what I'm looking for.

ANY of the images I've uploaded can be used as the actual front cover image OR the designer might have/find some suitable image to be used. The image is to be large and bold and fill the cover. Hopefully a positive energy.
It needs to be eye-catching and striking and bold and positive.

So...the book cover sample file I've provided can keep the back cover with completely new colouring. The front cover is completely new with new image, wording and energy.

It is to be a rainbow coloured face or figure for the cover image.

I hope that is clear enough for you. I'm very happy to discuss and clarify these ideas with the designer. Looking forward to another great PixelGuild experience.

Target Market(s)

Wide audience with special focus on Same Sex Attracted individuals

Font styles to use
Script
Other font styles liked:
• Some form of handwriting font to make the book title and text appear more personal....as if handwritten by me.

Requirements
Must have
• Boldness, Quirky, Rainbow Colour, Image to fill the cover, maybe dark cover contrasting background.
Nice to have
• A well balanced back cover especially in the area where the barcode will be placed.
Should not have
• No stereotypical images

```html
<!DOCTYPE html>
<html lang="en">
<head>
<meta charset="utf-8">
<title>The Open Meadow – Book Cover</title>
<link rel="stylesheet" href="https://fonts.googleapis.com/css2?family=Rubik+Dirt&family=Josefin+Sans:wght@600;700&display=swap">
<style>
  :root {
    --page-bg: #e6e6e6;
    --ink-black: #111111;
    --ink-white: #ffffff;
    --author-yellow: #f6e21a;
    --spine-teal: #1f3b3e;
    --back-teal: #28494b;
    --back-orange: #d9641c;
    --back-pink: #d98aa6;
    --front-red: #d8262a;
    --front-orange: #f08a1c;
    --front-yellow: #f4d21c;
    --front-blue: #2a6fd6;
    --front-cyan: #25b5c9;
    --front-magenta: #c8308c;
  }
  * { margin: 0; padding: 0; box-sizing: border-box; }
  html, body {
    width: 1200px;
    height: 848px;
    overflow: hidden;
    background: var(--page-bg);
  }
  .canvas {
    position: relative;
    width: 1200px;
    height: 848px;
  }
  .cover-spread {
    position: absolute;
    left: 120px;
    top: 70px;
    width: 960px;
    height: 710px;
    display: flex;
  }
  .back-cover {
    width: 444px;
    height: 100%;
    background:
      radial-gradient(ellipse 40% 18% at 50% 48%, var(--back-orange) 0%, transparent 70%),
      radial-gradient(ellipse 50% 14% at 50% 22%, var(--back-orange) 0%, transparent 75%),
      radial-gradient(ellipse 40% 20% at 50% 82%, var(--back-pink) 0%, transparent 70%),
      linear-gradient(180deg, var(--back-teal) 0%, #33585a 55%, #8fa3a6 100%);
  }
  .spine {
    width: 48px;
    height: 100%;
    background: var(--spine-teal);
    position: relative;
  }
  .spine-text {
    position: absolute;
    left: 50%;
    top: 28px;
    transform: translateX(-50%);
    writing-mode: vertical-rl;
    font-family: "Josefin Sans", sans-serif;
    font-weight: 700;
    display: flex;
    align-items: center;
    gap: 40px;
  }
  .spine-title {
    color: var(--ink-white);
    font-size: 26px;
    letter-spacing: 5px;
  }
  .spine-author {
    color: var(--author-yellow);
    font-size: 18px;
    letter-spacing: 3px;
  }
  .front-cover {
    position: relative;
    flex: 1;
    height: 100%;
    overflow: hidden;
  }
  .front-art {
    position: absolute;
    inset: 0;
    background:
      radial-gradient(ellipse 30% 40% at 50% 55%, var(--front-orange) 0%, transparent 70%),
      radial-gradient(ellipse 40% 25% at 20% 30%, var(--front-yellow) 0%, transparent 70%),
      radial-gradient(ellipse 35% 30% at 85% 45%, var(--front-blue) 0%, transparent 70%),
      radial-gradient(ellipse 40% 30% at 20% 75%, var(--front-cyan) 0%, transparent 70%),
      radial-gradient(ellipse 40% 25% at 80% 85%, var(--front-magenta) 0%, transparent 70%),
      linear-gradient(160deg, var(--front-yellow) 0%, var(--front-red) 45%, var(--front-blue) 100%);
  }
  .book-title {
    position: absolute;
    left: 30px;
    top: 12px;
    font-family: "Rubik Dirt", sans-serif;
    color: var(--ink-black);
    font-size: 70px;
    line-height: 0.98;
    letter-spacing: 2px;
    text-transform: uppercase;
  }
  .subtitle {
    position: absolute;
    font-family: "Josefin Sans", sans-serif;
    font-weight: 700;
    color: var(--ink-white);
    text-transform: uppercase;
    line-height: 1.02;
    text-shadow: 0 1px 3px rgba(0,0,0,0.25);
  }
  .subtitle-left { left: 50px; top: 270px; text-align: center; }
  .subtitle-right { right: 40px; top: 250px; text-align: center; }
  .subtitle .small { font-size: 30px; display: block; }
  .subtitle .large { font-size: 46px; display: block; }
  .author-name {
    position: absolute;
    left: 0;
    right: 0;
    bottom: 34px;
    text-align: center;
    font-family: "Josefin Sans", sans-serif;
    font-weight: 700;
    font-size: 38px;
    letter-spacing: 4px;
    color: var(--author-yellow);
    text-transform: uppercase;
  }
</style>
</head>
<body>
  <main class="canvas">
    <section class="cover-spread">
      <div class="back-cover" role="img" aria-label="Mirrored abstract painted artwork in teal, orange and pink tones"></div>

      <div class="spine">
        <div class="spine-text">
          <span class="spine-title">THE OPEN MEADOW</span>
          <span class="spine-author">ROWAN ELLERY</span>
        </div>
      </div>

      <div class="front-cover">
        <div class="front-art" role="img" aria-label="Boldly painted rainbow-coloured portrait filling the front cover"></div>
        <h1 class="book-title">The Open<br>Meadow</h1>
        <p class="subtitle subtitle-left">
          <span class="small">Walking</span>
          <span class="large">Forward</span>
          <span class="large">Beyond</span>
        </p>
        <p class="subtitle subtitle-right">
          <span class="small">Every</span>
          <span class="large">Box</span>
        </p>
        <p class="author-name">Rowan Ellery</p>
      </div>
    </section>
  </main>
</body>
</html>
```